Home page makeover

Take my existing home page, www.maplecrestledger.com and redesign layout to look more current considering today's touch design prevalence.
Reuse existing elements or suggest improved ones if available.
I generally have average CSS and HTML skills using div containers, defining lists and using columns to create the code to support the layout.
Updates
Just wanted to send out a quick message to thank all of you for your submissions. Many of you offered nice designs, but unfortunately could only choose one.
Target Market(s)
Generally targeting individuals with some assets for retirement. Basically your average working professional or business owner.
Industry/Entity Type
It Support
Look and feel
Each slider illustrates characteristics of the customer's brand and the style your logo design should communicate.

```html
<!DOCTYPE html>
<html lang="en">
<head>
<meta charset="utf-8">
<title>Maplecrest Ledger – Identify, Plan, Retire</title>
<link href="https://fonts.googleapis.com/css2?family=Gelasio:wght@400;700&family=Open+Sans:wght@400;600&family=Oswald:wght@400&display=swap" rel="stylesheet">
<style>
:root{
  --green-dark:#2f7410;
  --green:#43901a;
  --green-light:#5fae2c;
  --green-text:#3c8a17;
  --lime:#c8e86a;
  --hero-bg:#e4f0d6;
  --band-bg:#f3f3f3;
  --text:#444;
  --muted:#666;
  --footer:#333;
  --white:#fff;
}
*{box-sizing:border-box;margin:0;padding:0}
html,body{width:1103px;height:1200px;overflow:hidden}
body{position:relative;background:var(--white);font-family:"Open Sans",Arial,sans-serif;color:var(--text)}
.serif{font-family:Gelasio,Georgia,serif}

/* header */
.site-header{position:absolute;left:0;top:0;width:1103px;height:71px;background:linear-gradient(#4a9a1a,#38800f);box-shadow:0 2px 4px rgba(0,0,0,.25);z-index:2}
.brand{position:absolute;left:146px;top:10px;display:flex;align-items:center;gap:8px;color:var(--white);font-family:Gelasio,Georgia,serif}
.brand-mark{width:36px;height:36px;background:var(--white)}
.brand-name{font-size:30px;line-height:30px}
.brand-tag{position:absolute;left:52px;top:38px;font-size:9px;white-space:nowrap}
.account-links{position:absolute;right:148px;top:9px;font-family:Gelasio,Georgia,serif;font-size:13px;color:var(--lime)}
.account-links span{color:#a9d76a;margin:0 4px}
.main-nav{position:absolute;right:148px;top:41px;display:flex;gap:36px;font-family:Gelasio,Georgia,serif;font-size:14px;color:var(--white)}

/* hero */
.hero{position:absolute;left:0;top:71px;width:1103px;height:372px;background:radial-gradient(ellipse at 30% 40%,#f6f2ea 0%,#eef3e2 45%,var(--hero-bg) 100%)}
.hero-photo{position:absolute;left:100px;top:0;width:485px;height:372px;background:radial-gradient(ellipse at 55% 45%,#d9cdb8 0%,#cfc6b2 30%,#e8e6d8 65%,rgba(232,240,220,0) 100%)}
.hero-title{position:absolute;left:157px;top:261px;width:361px;height:42px;background:rgba(255,255,255,.82);font-family:Gelasio,Georgia,serif;font-size:25px;color:var(--green-text);padding:6px 0 0 20px;letter-spacing:.3px}
.video{position:absolute;left:586px;top:44px;width:370px;height:271px;background:#111;box-shadow:0 12px 14px -8px rgba(0,0,0,.35)}
.video-bar{height:25px;display:flex;align-items:center;justify-content:space-between;padding:0 10px;font-size:11px;color:#eee}
.video-frame{height:217px;background:linear-gradient(135deg,#d8d4c6 0%,#b9b6a6 40%,#ece9df 70%,#cfcfc9 100%)}
.video-progress{position:relative;height:6px;background:#555}
.video-progress i{position:absolute;left:0;top:0;width:113px;height:6px;background:#d01b1b}
.video-progress b{position:absolute;left:113px;top:-3px;width:12px;height:12px;border-radius:50%;background:#ddd}
.video-controls{height:23px;display:flex;align-items:center;gap:10px;padding:0 10px;font-size:10px;color:#ddd}

/* features */
.features{position:absolute;left:0;top:443px;width:1103px;height:214px;background:var(--band-bg);border-bottom:2px solid #e6e6e6}
.feature{position:absolute;top:34px;width:200px;text-align:center}
.feature h3{font-family:Gelasio,Georgia,serif;font-weight:400;font-size:16px;line-height:19px;color:var(--green-text);height:54px}
.feature p{font-size:11.5px;line-height:15.5px;color:var(--muted)}

/* testimonials */
.testimonials{position:absolute;left:145px;top:700px;width:536px}
.section-title{display:flex;align-items:center;gap:10px;height:46px;border-bottom:1px solid #ccc;padding-left:5px}
.section-title .orb{width:32px;height:32px;border-radius:50%;background:radial-gradient(circle at 40% 35%,#fff,#bbb 70%,#999)}
.section-title h2{font-family:Gelasio,Georgia,serif;font-size:19px;color:var(--green-text)}
.quote{position:relative;padding-left:37px;margin-top:19px}
.quote::before{content:"\201C";position:absolute;left:5px;top:-14px;font-family:Gelasio,Georgia,serif;font-size:50px;color:#bbb}
.quote p{font-size:12px;line-height:15.5px;color:#444}
.quote cite{display:block;text-align:right;font-style:normal;font-size:11px;margin-top:14px;color:var(--green-text)}
.quote cite span{color:#222}
.read-all{position:absolute;left:147px;top:1041px;width:76px;height:20px;background:linear-gradient(#4c9a1e,#2f7410);color:var(--white);font-family:Gelasio,Georgia,serif;font-size:11px;text-align:center;line-height:20px;border-radius:2px}

/* signup */
.signup{position:absolute;left:719px;top:720px;width:219px;height:305px;border-radius:14px;background:linear-gradient(#fff,#e7f2dc);border:1px solid #d4e6c4;box-shadow:0 14px 12px -10px rgba(0,0,0,.3);text-align:center}
.signup-head{position:absolute;left:-1px;top:-1px}
.signup-head span{position:absolute;left:0;top:9px;width:219px;font-family:Gelasio,Georgia,serif;font-weight:700;font-size:20px;color:var(--white)}
.price{position:absolute;left:0;top:62px;width:219px;font-size:12px;line-height:17px;color:#333}
.price strong{font-family:Oswald,sans-serif;font-weight:400;font-size:18px;color:var(--green-dark)}
.divider{position:absolute;left:10px;top:134px;width:199px;border-top:1px solid #cfdcc4}
.field{position:absolute;left:12px;width:196px;text-align:left;font-size:11.5px;color:#333}
.field label{display:block;margin:0 0 3px 3px}
.field span{display:block;height:26px;background:var(--white);border:1px solid #c9dcbc;border-radius:3px}
.signup-btn{position:absolute;left:33px;top:254px;width:148px;height:32px;border:2px solid #a8d486;border-radius:4px;background:linear-gradient(#4e9b22,#2f7410);font-family:Gelasio,Georgia,serif;font-weight:700;font-size:16px;color:var(--white);line-height:28px}

/* footer */
.site-footer{position:absolute;left:0;top:1101px;width:1103px;height:99px;background:var(--footer);text-align:center;font-family:Arial,sans-serif;font-size:11px;color:#aaa}
.footer-nav{padding-top:27px}
.footer-nav span{margin:0 5px}
.footer-rule{width:820px;height:1px;margin:14px auto 0;background:linear-gradient(90deg,transparent,#555,transparent)}
.copyright{margin-top:12px}
</style>
</head>
<body>

<header class="site-header">
  <div class="brand">
    <div class="brand-mark"></div>
    <div class="brand-name">Maplecrest</div>
    <div class="brand-tag">Plan Ahead</div>
  </div>
  <div class="account-links">Sign In<span>|</span>Sign Up</div>
  <nav class="main-nav"><a>Home</a><a>About</a><a>Contact</a></nav>
</header>

<section class="hero">
  <div class="hero-photo" role="img" aria-label="Photo of a smiling retired couple outdoors in autumn"></div>
  <div class="hero-title">IDENTIFY, PLAN, RETIRE</div>
  <div class="video">
    <div class="video-bar"><span>Any Title</span>
      <svg width="32" height="14" viewBox="0 0 32 14"><circle cx="3" cy="7" r="2" fill="#fff"/><circle cx="11" cy="3" r="2" fill="#fff"/><circle cx="11" cy="11" r="2" fill="#fff"/><path d="M3 7L11 3M3 7L11 11" stroke="#fff" stroke-width="1.3"/><circle cx="26" cy="7" r="6" fill="#fff"/><rect x="25" y="6" width="2" height="5" fill="#111"/><rect x="25" y="3" width="2" height="2" fill="#111"/></svg>
    </div>
    <div class="video-frame" role="img" aria-label="Video still of banknotes, a pen and financial charts"></div>
    <div class="video-progress"><i></i><b></b></div>
    <div class="video-controls">
      <svg width="14" height="14" viewBox="0 0 14 14"><path d="M2 1L13 7L2 13Z" fill="#ccc"/></svg>
      <svg width="18" height="14" viewBox="0 0 18 14"><path d="M1 5H4L8 1V13L4 9H1Z" fill="#ccc"/><path d="M11 4Q14 7 11 10M13 2Q17 7 13 12" stroke="#ccc" fill="none"/></svg>
      <span>0:42 <span style="color:#888">/ 3:20</span></span>
      <span style="flex:1"></span>
      <svg width="12" height="12" viewBox="0 0 12 12"><rect x="1" y="1" width="3" height="3" fill="#ccc"/><rect x="8" y="1" width="3" height="3" fill="#ccc"/><rect x="1" y="8" width="3" height="3" fill="#ccc"/><rect x="8" y="8" width="3" height="3" fill="#ccc"/></svg>
    </div>
  </div>
</section>

<section class="features">
  <div class="feature" style="left:140px"><h3>Identify and project your retirement</h3><p>... needs and expectations including basic living expenses, housing costs, recreation, big ticket non-recurring items, medical and nursing home care.</p></div>
  <div class="feature" style="left:347px"><h3>Identify and project all your sources</h3><p>of retirement income including retirement savings, other savings, pension plans, Social Security, life insurance and working part-time during retirement for a period of time.</p></div>
  <div class="feature" style="left:557px"><h3>Strategize tapping into the equity</h3><p>of your real estate including swapping your primary residence for a different home or retirement area, or selling and renting.</p></div>
  <div class="feature" style="left:763px"><h3>Produce easy to understand results</h3><p>featuring the Retirement Readiness Gauge™.</p></div>
</section>

<section class="testimonials">
  <div class="section-title"><div class="orb"></div><h2>Testimonials</h2></div>
  <div class="quote"><p>Etiam rhoncus. Maecenas tempus, tellus eget condimentum rhoncus, sem quam semper libero, sit amet commodo ligula eget dolor adipiscing sem neque sed ipsum.</p><cite>Daniel Hartwell, &nbsp;<span>Brightfield Co</span></cite></div>
  <div class="quote" style="margin-top:25px"><p>Etiam rhoncus. Maecenas tempus, tellus eget condimentum rhoncus, sem quam semper libero, sit amet adipiscing sem neque sed ipsum. Nam quam nunc, blandit vel, luctus pulvinar, hendrerit id, lorem. Maecenas nec odio et ante tincidunt tempus. Donec vitae sapien ut libero venenatis faucibus. Nullam quis ante.</p><cite style="margin-top:6px">Daniel Hartwell, &nbsp;<span>Brightfield Co</span></cite></div>
  <div class="quote" style="margin-top:34px"><p>Etiam rhoncus. Maecenas tempus, tellus eget condimentum rhoncus, sem quam semper libero, sit amet commodo ligula eget dolor adipiscing sem neque sed ipsum.</p><cite>Daniel Hartwell, &nbsp;<span>Brightfield Co</span></cite></div>
</section>
<a class="read-all">Read All »</a>

<aside class="signup">
  <svg class="signup-head" width="219" height="56" viewBox="0 0 219 56"><path d="M14 0H205Q219 0 219 14V36L109.5 56L0 36V14Q0 0 14 0Z" fill="#3f8a18"/></svg>
  <div class="signup-head"><span>SIGN UP</span></div>
  <div class="price">Only <strong>$19.99</strong><br>For a One Year Membership<br>Only <strong>$9.99</strong> Per Year After That</div>
  <div class="divider"></div>
  <div class="field" style="top:143px"><label>Your Name</label><span></span></div>
  <div class="field" style="top:193px"><label>Your email</label><span></span></div>
  <div class="signup-btn">SIGN UP</div>
</aside>

<footer class="site-footer">
  <div class="footer-nav">Home<span>I</span>About Us<span>I</span>Contact</div>
  <div class="footer-rule"></div>
  <div class="copyright">Copyright © 2013 Maplecrest Ledger, Inc. All rights reserved</div>
</footer>

</body>
</html>
```